Design an Elegant Handbag Brand website

I need a webiste design are looking for ideas for a new theme, color scheme, etc. You come up with the general look and feel of the home page and our team will take it from there.
We're only looking for a one (1) page layout which should be fashionable and graphic intensive, but also include the standard homepage links (about us, see our collections, etc)

Target Market(s)

Our customers are fashionable women looking for an animal friendly and environmentally friendly handbag.

Industry/Entity Type

Business

Number of Pages Required

1 page

Font styles to use
Serif
Sans Serif

Requirements
Must have
• Feel free to modify it with different colors or tweaks as you see fit. We are open to all suggestions.
Nice to have

```html
<!DOCTYPE html>
<html lang="en">
<head>
<meta charset="utf-8">
<title>Velora — Handbags</title>
<link href="https://fonts.googleapis.com/css2?family=Playfair+Display:wght@400&family=Roboto:ital,wght@0,300;0,400;0,500;1,400&display=swap" rel="stylesheet">
<style>
:root{
  --orange:#ff6a00;
  --orange-soft:#ff9a4d;
  --peach:#fdd7b5;
  --peach-light:#fff3e8;
  --ink:#2c2f3e;
  --text:#333;
  --muted:#777;
  --grey-bg:#f5f5f5;
  --footer:#232323;
  --footer-text:#bdbdbd;
}
*{box-sizing:border-box;margin:0;padding:0}
html,body{width:1200px;height:2545px;overflow:hidden;background:#fff}
.page{position:relative;width:1215px;height:2576px;transform:scale(0.98765);transform-origin:0 0;font-family:'Roboto',sans-serif;color:var(--text)}
.abs{position:absolute}
.serif{font-family:'Playfair Display',serif;font-weight:400;color:var(--ink)}
.underline::after{content:"";position:absolute;left:2px;bottom:-8px;width:46px;height:2px;background:var(--orange)}

/* header */
.site-header{left:0;top:0;width:1215px;height:78px;background:#fff}
.brand{left:93px;top:18px;font-size:30px}
.nav{left:497px;top:47px;display:flex;gap:0;font-family:'Playfair Display',serif;font-size:14px;color:var(--ink)}
.nav a{color:inherit;text-decoration:none;position:absolute;white-space:nowrap}
.nav a.active::after{content:"";position:absolute;left:0;bottom:-8px;width:14px;height:2px;background:var(--orange)}
.header-icons svg{position:absolute}
.cart-badge{left:1065px;top:40px;width:14px;height:14px;border-radius:50%;background:var(--orange);color:#fff;font-size:8px;text-align:center;line-height:14px}

/* hero */
.hero{left:0;top:78px;width:1215px;height:578px;background:linear-gradient(180deg,var(--peach) 0%,#fff4ea 50%,var(--peach) 100%);overflow:hidden}
.hero-photo{left:580px;top:0;width:600px;height:578px;background:linear-gradient(160deg,#e9d3c6 0%,#f2e6e3 40%,#2a2a33 70%,#1a1a1f 100%);border-radius:0}
.hero-title{left:172px;top:218px;font-size:46px;line-height:1.1;letter-spacing:0.5px}
.hero-title::after{width:75px}
.hero-text{left:172px;top:296px;width:436px;font-size:14px;line-height:18px;text-align:center;color:#222}
.btn-discover{left:270px;top:362px;width:240px;height:56px;border-radius:28px;background:var(--orange);color:#fff;font-size:26px;letter-spacing:2px;text-align:center;line-height:56px}
.dots{left:590px;top:629px;display:flex;gap:8px}
.dots span{width:6px;height:6px;border-radius:50%;background:var(--orange)}
.dots span:first-child{background:#fff}

/* about */
.about-frame{left:212px;top:635px;width:258px;height:415px;border-left:16px solid var(--orange);border-top:10px solid var(--orange)}
.about-photo{left:228px;top:649px;width:284px;height:426px;background:linear-gradient(180deg,#cfc6c0 0%,#a8a19d 45%,#8e7d74 70%,#c9c4c1 100%)}
.about-title{left:607px;top:700px;font-size:32px}
.about-text{left:614px;top:810px;width:408px;font-size:16px;line-height:19.3px;text-align:justify;color:#222}
.read-more{left:614px;top:983px;font-size:17px;color:var(--orange)}

/* products */
.featured-title{left:180px;top:1137px;font-size:33px}
.card{width:184px;height:283px;top:1243px;border:1px solid var(--orange-soft);background:#fff;text-align:center}
.card .product{position:absolute;left:12px;top:14px;width:160px;height:150px}
.card .price{position:absolute;left:0;right:0;top:192px;font-size:16px;font-weight:500;color:var(--orange)}
.card .name{position:absolute;left:0;right:0;top:211px;font-size:14px;color:#666}
.card .view{position:absolute;left:47px;top:239px;width:88px;height:29px;border:1px solid var(--orange);color:var(--orange);font-size:14px;line-height:27px}

/* collections */
.collections{left:0;top:1572px;width:1215px;height:403px;background:linear-gradient(180deg,var(--peach) 0%,#ffb57d 55%,var(--orange-soft) 100%);overflow:hidden}
.collections-photo{left:150px;top:0;width:330px;height:403px;background:linear-gradient(180deg,#b89a8e 0%,#b98a70 40%,#a7785e 70%,#8d8a88 100%)}
.collections-box{left:595px;top:1640px;width:416px;height:74px;background:var(--peach-light);box-shadow:-10px -6px 0 #f9b47c}
.collections-title{left:624px;top:1656px;font-size:33px}
.collections-title::after{width:38px;bottom:-6px}
.collections-text{left:571px;top:1759px;width:464px;font-size:13.5px;line-height:17px;text-align:justify;text-align-last:center;color:#fff}
.btn-view-all{left:709px;top:1861px;width:186px;height:33px;border:2px solid #fff;color:#fff;font-size:16px;font-weight:500;letter-spacing:8px;line-height:29px;padding-left:13px}

/* testimonials */
.testimonials{left:0;top:1975px;width:1215px;height:363px;background:var(--grey-bg)}
.testimonials-title{left:0;width:1215px;top:1998px;font-size:33px;text-align:center}
.testimonials-title::after{left:496px;width:42px}
.avatar{left:560px;top:2073px;width:96px;height:96px;border-radius:50%;background:linear-gradient(180deg,#8c8a88,#5d4e48 60%,#c06040)}
.quote{left:226px;top:2190px;width:764px;font-size:14px;line-height:17px;text-align:center;color:#777}
.author{left:0;width:1215px;top:2274px;font-family:'Playfair Display',serif;font-size:14px;color:var(--orange);text-align:center}
.quote-dots{left:589px;top:2317px;display:flex;gap:6px}
.quote-dots span{width:14px;height:1px;background:#999}

/* footer */
.site-footer{left:0;top:2338px;width:1215px;height:238px;background:var(--footer)}
.newsletter-title{left:0;width:1215px;top:2366px;text-align:center;font-family:'Playfair Display',serif;font-size:14px;color:#fff}
.email{left:440px;top:2403px;width:236px;height:36px;border:1px solid #888;border-radius:18px;font-size:12px;color:#aaa;line-height:34px;padding-left:19px}
.subscribe{left:685px;top:2403px;width:91px;height:36px;border-radius:18px;background:var(--orange);color:#fff;font-size:13px;font-weight:500;text-align:center;line-height:36px}
.footer-link{top:2471px;font-size:14px;color:var(--footer-text)}
.social{top:2471px;width:16px;height:16px;border-radius:50%;background:#fff}
.footer-rule{left:0;top:2518px;width:1215px;height:1px;background:#333}
.copyright{left:0;width:1215px;top:2535px;text-align:center;font-size:13px;font-style:italic;color:#777}
</style>
</head>
<body>
<div class="page">

  <header class="abs site-header">
    <div class="abs brand serif">Velora</div>
    <nav class="abs nav">
      <a class="active" style="left:0">HOME</a>
      <a style="left:88px">SHOP</a>
      <a style="left:171px">NEW ARRIVALS</a>
      <a style="left:313px">CONTACT</a>
    </nav>
    <div class="header-icons">
      <svg style="left:963px;top:42px" width="26" height="26" viewBox="0 0 26 26" fill="none" stroke="#111" stroke-width="2"><circle cx="11" cy="11" r="8"/><line x1="17" y1="17" x2="24" y2="24"/></svg>
      <svg style="left:1006px;top:43px" width="26" height="24" viewBox="0 0 26 24" fill="none" stroke="#111" stroke-width="1.8"><path d="M13 22 C4 15 1 11 1 7 a6 6 0 0 1 12-1 a6 6 0 0 1 12 1 c0 4-3 8-12 15z"/></svg>
      <svg style="left:1049px;top:42px" width="24" height="26" viewBox="0 0 24 26" fill="none" stroke="#111" stroke-width="1.8"><path d="M3 9h18l-1 15H4z"/><path d="M8 11V6a4 4 0 0 1 8 0v5"/></svg>
      <div class="abs cart-badge">1</div>
    </div>
  </header>

  <section class="abs hero">
    <svg class="abs" style="left:0;top:0" width="1215" height="578" fill="none" stroke="#f7b98a" stroke-width="1">
      <polyline points="0,30 138,168 0,306"/>
      <polyline points="1215,230 1000,445 1215,660"/>
    </svg>
    <div class="abs hero-photo" role="img" aria-label="Model in sunglasses and polka-dot blouse holding a black leather handbag"></div>
  </section>
  <h1 class="abs hero-title serif underline">THE FASHION WORLD</h1>
  <p class="abs hero-text">Fashion is a popular aesthetic expression at a particular time and in a specific context, especially in clothing, footwear, lifestyle</p>
  <div class="abs btn-discover">Discover Now</div>
  <div class="abs dots"><span></span><span></span><span></span></div>

  <svg class="abs" style="left:0;top:656px" width="1215" height="460" fill="none" stroke="#f6dcc6" stroke-width="1">
    <polyline points="1120,0 1215,80"/>
    <polygon points="1157,190 1280,315 1157,440 1032,315"/>
  </svg>
  <div class="abs about-frame"></div>
  <div class="abs about-photo" role="img" aria-label="Woman walking on a city street carrying a black tote bag"></div>
  <h2 class="abs about-title serif underline">ABOUT US</h2>
  <p class="abs about-text">We are the printing and typesetting industry. Lorem Ipsum has been the industry's standard dummy text ever since the 1500s, when an unknown printer took a galley of type and scrambled it to make a type specimen book. It has survived not only five centuries, but also the leap into electronic typesetting, remaining essentially unchanged. It was popularised in the 1960s with the release of Letraset sheets containing Lorem Ipsum passages, and..</p>
  <a class="abs read-more">Read more</a>

  <h2 class="abs featured-title serif underline">FEATURED PRODUCTS</h2>
  <svg class="abs" style="left:136px;top:1370px" width="40" height="28" fill="none" stroke="#999" stroke-width="2"><path d="M38 14H3M15 2L3 14l12 12"/></svg>
  <svg class="abs" style="left:1036px;top:1370px" width="40" height="28" fill="none" stroke="#999" stroke-width="2"><path d="M2 14h35M25 2l12 12-12 12"/></svg>

  <div class="abs card" style="left:203px"><div class="product" role="img" aria-label="Beige leather handbag set" style="background:linear-gradient(180deg,#fff 10%,#c8ad8c 40%,#a88a68 90%,#fff)"></div><div class="price">$101.25</div><div class="name">The leather bag</div><div class="view">View</div></div>
  <div class="abs card" style="left:411px"><div class="product" role="img" aria-label="Light blue leather handbag set" style="background:linear-gradient(180deg,#fff 10%,#8eb2d6 40%,#6a93bf 90%,#fff)"></div><div class="price">$101.25</div><div class="name">The leather bag</div><div class="view">View</div></div>
  <div class="abs card" style="left:619px"><div class="product" role="img" aria-label="Black leather tote bag" style="background:linear-gradient(180deg,#fff 5%,#2a2a2a 40%,#111 90%,#fff)"></div><div class="price">$101.25</div><div class="name">The leather bag</div><div class="view">View</div></div>
  <div class="abs card" style="left:827px"><div class="product" role="img" aria-label="Grey leather handbag set" style="background:linear-gradient(180deg,#fff 10%,#9a9a9a 40%,#7d7d7d 90%,#fff)"></div><div class="price">$101.25</div><div class="name">The leather bag</div><div class="view">View</div></div>

  <section class="abs collections">
    <svg class="abs" style="left:0;top:0" width="1215" height="403" fill="none" stroke="#f26a10" stroke-width="1">
      <polyline points="0,160 142,20 300,178"/>
      <polyline points="0,180 140,322"/>
      <polyline points="1215,120 1047,288 1160,403"/>
    </svg>
    <div class="abs collections-photo" role="img" aria-label="Woman in floral blouse holding a tan leather tote bag"></div>
  </section>
  <div class="abs collections-box"></div>
  <h2 class="abs collections-title serif underline">SEE OUR COLLECTIONS</h2>
  <p class="abs collections-text">It is a long established fact that a reader will be distracted by the readable content of a page when looking at its layout. The point of using Lorem Ipsum is that it has a more-or-less normal distribution of letters, as opposed to using 'Content here, content</p>
  <div class="abs btn-view-all">VIEW ALL<svg style="position:absolute;right:12px;top:7px" width="28" height="16" fill="none" stroke="#fff" stroke-width="1.6"><path d="M0 8h26M19 1l7 7-7 7"/></svg></div>

  <section class="abs testimonials"></section>
  <h2 class="abs testimonials-title serif underline">TESTIMONIALS</h2>
  <div class="abs avatar" role="img" aria-label="Customer portrait"></div>
  <p class="abs quote">"Neque porro quisquam est qui dolorem ipsum quia dolor sit amet, consectetur, adipisci velit There is no one who loves pain itself, who seeks after it and wants to have it, simply because it is pain neque porro quisquam est qui dolorem ipsum quia dolor sit amet, consectetur, adipisci velit.There is no one who loves pain itself, who seeks after it and wants to have it, simply because it is pain.</p>
  <div class="abs author">-MARA VELLINI</div>
  <div class="abs quote-dots"><span></span><span></span></div>

  <footer class="abs site-footer"></footer>
  <div class="abs newsletter-title">JOIN OUR NEWSLETTER</div>
  <div class="abs email">Enter your email address</div>
  <div class="abs subscribe">Subscribe</div>
  <a class="abs footer-link" style="left:399px">Terms &amp; Condition</a>
  <a class="abs footer-link" style="left:573px">Privacy Policy</a>
  <span class="abs social" style="left:722px" aria-label="Social link"></span>
  <span class="abs social" style="left:760px" aria-label="Social link"></span>
  <span class="abs social" style="left:798px" aria-label="Social link"></span>
  <div class="abs footer-rule"></div>
  <div class="abs copyright">© 2020 Velora Atelier. All rights reserved.</div>

</div>
</body>
</html>
```